Brochure/Catalog for Door Manufacturer and Designer

Marlowe Door Design is a door manufacturer and distributor based out of the Southwest United States. We need a catalog showcasing our four door collections.
We have a clear vision on what the catalog will look like (SEE INSTRUCTIONS ATTACHED), but we need a creative designer to put it all together.
We have attached:
Please read the attached brochure instructions and contact us with any questions.
Thank you for your time and we look forward to seeing your design!
Marlowe Door Design

```html
<!DOCTYPE html>
<html lang="en">
<head>
<meta charset="utf-8">
<title>Marlowe Door Design — Collection Catalogue 2014</title>
<link rel="stylesheet" href="https://fonts.googleapis.com/css2?family=Cinzel:wght@400&family=Questrial&display=swap">
<style>
  :root {
    --paper: #ddd6c0;
    --frame-red: #861c1f;
    --label-black: #0c0c0c;
    --label-text: #ffffff;
    --title-ink: #141414;
  }
  * { margin: 0; padding: 0; box-sizing: border-box; }
  html, body {
    width: 927px;
    height: 1200px;
    overflow: hidden;
    background: var(--paper);
  }
  .cover {
    position: relative;
    width: 927px;
    height: 1200px;
    background: var(--paper);
  }
  .brand-name {
    position: absolute;
    left: 0;
    right: 0;
    top: 540px;
    text-align: center;
    font-family: "Questrial", sans-serif;
    font-weight: 400;
    font-size: 34px;
    line-height: 1.2;
    letter-spacing: 0.5px;
    color: var(--title-ink);
    white-space: nowrap;
  }
  .title-band {
    position: absolute;
    left: 73px;
    top: 848px;
    width: 815px;
    height: 123px;
    border: 4px solid var(--frame-red);
  }
  .title-band-inner {
    position: absolute;
    left: 4px;
    top: 4px;
    right: 4px;
    bottom: 4px;
    border: 3px solid var(--frame-red);
  }
  .edition-label {
    position: absolute;
    left: 4px;
    top: 6px;
    width: 218px;
    height: 86px;
    background: var(--label-black);
    color: var(--label-text);
    font-family: "Questrial", sans-serif;
    text-align: center;
    display: flex;
    flex-direction: column;
    justify-content: center;
    line-height: 1.35;
  }
  .edition-label .line { font-size: 18px; letter-spacing: 0.3px; }
  .edition-label .year { font-size: 22px; }
  .collection-title {
    position: absolute;
    left: 222px;
    right: 0;
    top: 0;
    bottom: 0;
    display: flex;
    align-items: center;
    justify-content: center;
    font-family: "Cinzel", serif;
    font-weight: 400;
    font-size: 37px;
    letter-spacing: 0.5px;
    color: var(--title-ink);
    white-space: nowrap;
  }
</style>
</head>
<body>
  <main class="cover">
    <h1 class="brand-name">Marlowe Door Design</h1>

    <section class="title-band">
      <div class="title-band-inner">
        <div class="edition-label">
          <span class="line">COLLECTION</span>
          <span class="line">CATALOGUE</span>
          <span class="year">2014</span>
        </div>
        <h2 class="collection-title">CUSTOM WOOD DOORS</h2>
      </div>
    </section>
  </main>
</body>
</html>
```